INSURANCE
RAY HOLLOWAY INSURANCE
Project: INSURANCE
INSURANCE -
Creative Brief
Cutting-Edge
20837 MAPLECREST DR SUITE 210 DALLAS TX 75251
rhollowayinsurance@mailvexo.com
rateyourcover.com
I am open for any suggestions on the Design type... On the back of the card "YOU" should stand out OR should be a larger Font.
ARE YOU TIRED OF PAYING TOO MUCH FOR INSURANCE..?? OUR EXPERTISE IN SHOPPING MULTIPLE PROVIDERS WILL SAVE "YOU" MONEY...$$

```html
<!DOCTYPE html>
<html lang="en">
<head>
<meta charset="utf-8">
<title>Ray Holloway Insurance – Business Card</title>
<link href="https://fonts.googleapis.com/css2?family=Cinzel:wght@400;700&family=Arimo:wght@400&display=swap" rel="stylesheet">
<style>
  :root {
    --stage: #dcdcdc;
    --card-blue: #1a80ad;
    --ink-white: #ffffff;
    --ink-dark: #0c2f45;
    --accent-yellow: #f2e600;
    --accent-red: #d8211f;
    --mark-navy: #1f3f78;
  }
  * { margin: 0; padding: 0; box-sizing: border-box; }
  html, body { width: 1200px; height: 925px; overflow: hidden; background: var(--stage); }
  .canvas { position: relative; width: 1200px; height: 925px; }

  .card {
    position: absolute;
    left: 270px;
    width: 680px;
    background: var(--card-blue);
    color: var(--ink-white);
  }
  .card--front { top: 45px; height: 387px; }
  .card--back  { top: 470px; height: 392px; }

  /* Front */
  .brand-mark {
    position: absolute; left: 260px; top: 50px;
    width: 160px; height: 160px; border-radius: 50%;
    background: var(--ink-white);
    display: flex; align-items: center; justify-content: center; text-align: center;
    font-family: "Cinzel", serif; font-weight: 700; font-size: 17px; line-height: 1.25;
    color: var(--mark-navy);
  }
  .front-title {
    position: absolute; left: 0; right: 0; top: 222px; text-align: center;
    font-family: "Cinzel", serif; font-size: 31px; letter-spacing: 0.5px;
  }
  .contact {
    position: absolute; left: 167px; top: 300px;
    font-family: "Arimo", sans-serif; color: var(--ink-dark);
  }
  .contact p { font-size: 15px; line-height: 20px; }
  .contact .contact-email { font-size: 10.5px; line-height: 18px; }

  /* Back */
  .pitch {
    position: absolute; left: 80px; top: 50px;
    font-family: "Cinzel", serif; font-weight: 700; font-size: 13px; line-height: 20px;
    color: var(--accent-yellow);
  }
  .pitch .pitch-you { font-size: 17px; }
  .back-title {
    position: absolute; left: 130px; top: 102px;
    font-family: "Cinzel", serif; font-size: 28px;
  }
  .services {
    position: absolute; left: 130px; top: 150px;
    font-family: "Cinzel", serif; color: var(--ink-dark);
  }
  .services h3 { font-weight: 400; font-size: 22px; line-height: 28px; }
  .services .services-intro { font-size: 13px; line-height: 26px; margin-bottom: 6px; }
  .services ol { list-style: none; font-size: 14px; line-height: 27px; }

  .seal-mark {
    position: absolute; left: 400px; top: 150px;
    width: 172px; height: 172px; border-radius: 50%;
    border: 5px solid rgba(12,47,69,0.55);
    display: flex; align-items: center; justify-content: center; text-align: center;
    font-family: "Cinzel", serif; font-weight: 700; font-size: 18px; line-height: 1.3;
    color: rgba(12,47,69,0.55);
  }

  .offer {
    position: absolute; left: 0; top: 332px; right: 0;
    font-family: "Cinzel", serif; font-size: 13px; color: var(--ink-white);
  }
  .offer-line { display: flex; align-items: center; height: 22px; }
  .offer-free {
    background: var(--accent-red); width: 118px; height: 22px;
    display: flex; align-items: center; justify-content: flex-end; padding-right: 4px;
    font-size: 16px;
  }
  .offer-text { padding-left: 4px; }
  .offer-cta { padding-left: 30px; line-height: 24px; }
</style>
</head>
<body>
<main class="canvas">

  <section class="card card--front" aria-label="Card front">
    <div class="brand-mark">Ray<br>Holloway<br>Insurance</div>
    <h1 class="front-title">RAY HOLLOWAY INSURANCE</h1>
    <div class="contact">
      <p>20837 Maplecrest Dr Ste 210 &nbsp;Dallas TX 75251</p>
      <p>Phone : 972-555-0184 Fax : 214-555-0127</p>
      <p class="contact-email">Email : rhollowayinsurance@mailvexo.com, www.rateyourcover.com</p>
    </div>
  </section>

  <section class="card card--back" aria-label="Card back">
    <div class="pitch">
      <p>ARE YOU TIRED OF PAYING TOO MUCH FOR INSURANCE..??</p>
      <p>OUR EXPERTISE IN SHOPPING MULTIPLE PROVIDERS WILL SAVE <span class="pitch-you">"YOU"</span> MONEY...$$</p>
    </div>
    <div class="seal-mark">Ray Holloway<br>Insurance</div>
    <h2 class="back-title">RAY HOLLOWAY INSURANCE</h2>
    <div class="services">
      <h3>Services</h3>
      <p class="services-intro">We provide the following:</p>
      <ol>
        <li>1. Auto Insurance</li>
        <li>2. Home Insurance</li>
        <li>3. Life Insurance</li>
        <li>4. Health Insurance</li>
      </ol>
    </div>
    <div class="offer">
      <div class="offer-line">
        <span class="offer-free">FREE</span>
        <span class="offer-text">no-obligation cost comparison of your current coverages.</span>
      </div>
      <p class="offer-cta">Request a Quote Online</p>
    </div>
  </section>

</main>
</body>
</html>
```